Nestivo Homes from US$9,995– Making buying a house as easy as ordering a pizza online - worldwide

I am after a website that is fun and interactive.

Buying a house should be as simple as buying a Pizza delivery online.....

Margherita 20' ………………………………………….US$9,995
Standard, 30sqm Studio with kitchen & Bathroom, Flat Roof
Four Cheese 20' ………………………………………….US$11,995
Standard, 30sqm Studio with kitchen & Bathroom, Pitched Roof
Supreme 40' ………………………………………….US$18,995
Standard, 60sqm, 2 Bedrooms, Lounge, kitchen & Bathroom, Flat Roof
Pepperoni 40' ………………………………………….US$20,995
Standard, 60sqm, 2 Bedrooms, Lounge, kitchen & Bathroom, Pitched Roof
Hawaiian 40' ………………………………………….US$22,995
Beach design, 60sqm, 2 Bedrooms, Lounge, kitchen & Bathroom, Pitched Roof
The Works 40' ………………………………………….US$24,995
Beach design, 60sqm, 2 Bedrooms, Lounge, kitchen, Bathroom, Deck, Pitched Roof

eg. https://www.snackroute.com.au/ https://www.crustbarn.com

I want a fun design....

i want to reinvent how people DESIGN - BUILD and DELIVER housing

I want a SaaS solution for drop shipping pre-built houses.

The main campaign, we are offering 1,000 homes (to anywhere in the world) for US$9,995 + shipping

Just need to Pay a Fully refundable $100 Deposit to pre-register (so need a shopping cart & payment solution).

"Queue Jumper" - pay in full and jump the queue to get your Nestivo months earlier.

The campaign is based on crowdsourcing - we need 1000 participants to pre-register - then everyone's orders will be filled .

The design is very simple...
HEADER
- The Story
- The Product
- Design our Own
- Pre-Register
- Contact Us

- Login
- Shopping Cart

FOOTER
- Privacy
- Terms & Conditions
- Investment
- Media
- NGO/Government
- Contact
- Sitemap

The important parts is that everyone who
- Subscribes
- Makes Contact
- Pre-registers
…in the system automatically gets an account (just need name and email address).
The user is then sent an email with details on how they can log back in at any time and see purchases, update profile (eg. Shipping address, contact details, etc....)

This data also needs to be sent to a CRM eg Lumatrak for marketing to automate regular updates to all users.

It also needs to link to Chatterly, WorkLoop , ZipZap, Pictova, Chirpex

You can get sample content from our old website https://modularhomes.webnestly.com/ - Plus I have attached updated content in this Brief.

The hero image should be a slider with videos and images with links to "Call to Action"

PLEASE NOTE: that "nestivo" is a brand new product that we pre build offsite so when it is delivered, it is ready to move in to. So we need a whole new look and a new style

This is a wordpress site to be hosted on my server - Once completed I need full access to add, amend and update any pages, images products

I am very open to different colours - do not be limited by the colours in the logo.

I would be interested to see what you can do with NO white backgrounds. (This might look good or could look horrible)

And most importantly what will your design look like on mobile devices (phones / ipads)

SUCCESS (1) is getting the user to LOOK - DREAM - BUY (Or at least pre-register)

SUCCESS (2) it MUST look fun but still highly professional and TRUSTWORTHY to get the interest of investors to invest millions $$$$$

SUCCESS (3) we need to get "Inflencers / Bloggers" talking about Nestivo - this could be done by a campaign to get a million likes and get a FREE home fo both the follower and the blogger

Target Market(s)

New home buyers (younger demographic), Families wanting to extend (middle aged)

Industry/Entity Type

Housing, Crowdsourcing, Drop shipping, SaaS technology

Coding

Coded - Design and coding required

Colors
0054AA
0677BA
7BADD7
CADEEF
E8F1F8
EE7325
F08F49
F5BC92
FAE3D3
FDF4ED

Requirements
Must have
• ecommerce, user accounts, social media & crm connections for crowdsourcing marketing, Call to actions
Nice to have
• $1,000,000
Should not have
• Do NOT complicate the funnel in the steps to sign-up

```html
<!DOCTYPE html>
<html lang="en">
<head>
<meta charset="utf-8">
<title>Nestivo — Design Build Deliver</title>
<link href="https://fonts.googleapis.com/css2?family=Open+Sans:wght@400;600;700;800&family=Roboto:wght@400;500&display=swap" rel="stylesheet">
<style>
:root{
  --brand:#0054AA;
  --brand-mid:#0677BA;
  --brand-soft:#5B8FCC;
  --ink:#0B1422;
  --ink-deep:#070C16;
  --white:#FFFFFF;
  --muted:#C9D0DA;
  --line:#7BADD7;
  --dark-btn:#0A0A0A;
}
*{box-sizing:border-box;margin:0;padding:0}
html,body{width:1200px;height:3038px;overflow:hidden}
body{font-family:"Open Sans",sans-serif;color:var(--white);background:var(--ink);position:relative}
.abs{position:absolute}

/* header */
.site-header{position:absolute;left:0;top:0;width:1200px;height:81px;background:var(--white);border-bottom:1px solid #d8dde4}
.brand-name{position:absolute;left:103px;top:18px;font-weight:800;font-size:36px;color:var(--brand);letter-spacing:1px}
.main-nav a{position:absolute;top:27px;font-size:19px;font-weight:600;color:#111;text-decoration:none}
.cart{position:absolute;left:1017px;top:27px;font-size:22px;color:var(--brand-mid);display:flex;gap:14px;align-items:center}

/* hero */
.hero{position:absolute;left:0;top:81px;width:1200px;height:598px;overflow:hidden}
.hero-copy{position:absolute;left:108px;top:168px}
.welcome{font-size:32px;font-weight:400;letter-spacing:1px}
.hero-title{font-size:96px;font-weight:800;line-height:1;margin-top:-2px;letter-spacing:1px}
.hero-tag{font-size:22px;letter-spacing:9px;margin-top:10px;font-weight:400;word-spacing:22px}
.btn-light{position:absolute;left:109px;top:349px;width:148px;height:50px;background:var(--white);color:var(--brand);border-radius:6px;font-size:17px;font-weight:600;display:flex;align-items:center;justify-content:center}

/* why choose */
.why{position:absolute;left:0;top:679px;width:1200px;height:747px;background:radial-gradient(ellipse at 50% 45%,#1a2536 0%,var(--ink) 55%,var(--ink-deep) 100%)}
.section-title{position:absolute;left:0;width:1200px;text-align:center;font-weight:700;font-size:36px}
.title-bar{position:absolute;left:568px;width:64px;height:4px;background:var(--white)}
.feature h3{position:absolute;font-size:26px;font-weight:700}
.feature p{position:absolute;font-family:"Roboto",sans-serif;font-size:12.5px;line-height:17.5px;color:var(--muted);width:260px}

/* services */
.services{position:absolute;left:0;top:1426px;width:1200px;height:611px;background:linear-gradient(180deg,#0a56a6 0%,#0f5cb0 60%,#0c57a8 100%)}
.services-curve{position:absolute;left:0;top:1426px}
.service-card{position:absolute;top:1595px;width:321px}
.service-photo{width:321px;height:288px;border-radius:12px}
.service-card h4{margin:14px 0 0 11px;font-size:22px;font-weight:700;line-height:29px;text-transform:uppercase}

/* offer */
.offer{position:absolute;left:0;top:2037px;width:1200px;height:568px;background:linear-gradient(180deg,#151515 0%,#1e1f22 50%,#121212 100%)}
.offer-line{position:absolute;left:0;width:1200px;text-align:center}
.newsletter{position:absolute;left:228px;top:2471px;width:743px;height:54px;background:var(--white);border-radius:5px;color:#222;font-size:17px;padding:16px 22px}

/* footer */
.site-footer{position:absolute;left:0;top:2605px;width:1200px;height:433px}
.footer-name{position:absolute;left:101px;top:2745px;font-size:54px;font-weight:800}
.payments{position:absolute;left:104px;top:2862px;width:261px;height:50px;background:var(--white);border-radius:12px;display:flex;align-items:center;justify-content:space-around;padding:0 10px;font-size:12px;font-weight:700;color:var(--brand)}
.foot-head{position:absolute;top:2700px;font-size:19px;font-weight:700}
.quick-links{position:absolute;left:406px;top:2741px;list-style:none;font-size:15px;line-height:24px}
.field{position:absolute;background:var(--white);border:1px solid #c7cfd9;color:#777;font-family:"Roboto",sans-serif;font-size:11px;padding:8px 11px}
.submit{position:absolute;left:1016px;top:2925px;width:84px;height:31px;background:var(--dark-btn);color:var(--white);border-radius:5px;font-size:13px;font-weight:700;display:flex;align-items:center;justify-content:center}
.copyright{position:absolute;left:97px;top:2996px;font-size:17px}
.socials{position:absolute;left:894px;top:2992px;display:flex;gap:14px}
.socials span{width:31px;height:31px;border-radius:50%;border:1.5px solid var(--white);display:flex;align-items:center;justify-content:center;font-size:13px;font-weight:700}
.socials span.filled{background:#000;border-color:#000}
</style>
</head>
<body>

<header class="site-header">
  <div class="brand-name">Nestivo</div>
  <nav class="main-nav">
    <a style="left:433px">The Story</a>
    <a style="left:562px">The Product</a>
    <a style="left:717px">Pre-Register</a>
    <a style="left:872px">Contact Us</a>
  </nav>
  <div class="cart">Cart
    <svg width="22" height="20" viewBox="0 0 22 20"><path d="M1 2h4l3 11h10l2-8H7" fill="none" stroke="#0677BA" stroke-width="2.5"/><circle cx="9" cy="17" r="2" fill="#0677BA"/><circle cx="17" cy="17" r="2" fill="#0677BA"/></svg>
  </div>
</header>

<section class="hero">
  <svg class="abs" style="left:0;top:0" width="1200" height="598">
    <defs>
      <linearGradient id="room" x1="0" y1="0" x2="1" y2="1">
        <stop offset="0" stop-color="#d9dde3"/><stop offset=".5" stop-color="#9aa1ab"/><stop offset="1" stop-color="#4a4f57"/>
      </linearGradient>
    </defs>
    <rect width="1200" height="598" fill="url(#room)" role="img" aria-label="Bright double-height living room with sofa, staircase and large black-framed windows"/>
    <path d="M0 0H599V250C590 420 510 560 365 598H0Z" fill="#5B8FCC" role="img" aria-label="Blue panel with faint architectural blueprint pattern"/>
    <path d="M1200 560C1130 560 1030 580 960 598H1200Z" fill="#0B1422"/>
  </svg>
  <div class="hero-copy">
    <div class="welcome">WELCOME TO</div>
    <div class="hero-title">NESTIVO</div>
    <div class="hero-tag">DESIGN BUILD DELIVER</div>
  </div>
  <div class="btn-light">PRE-REGISTER</div>
</section>

<section class="why">
  <div class="section-title" style="top:80px">WHY CHOOSE NESTIVO</div>
  <div class="title-bar" style="top:127px"></div>

  <svg class="abs" style="left:0;top:0" width="1200" height="747">
    <g fill="none" stroke="#55647a" stroke-width="1" stroke-dasharray="4 3">
      <path d="M193 205H455L500 260"/><path d="M193 380H430L446 380"/><path d="M193 555H455L500 500"/>
      <path d="M1007 205H745L700 260"/><path d="M1007 380H770L754 380"/><path d="M1007 555H745L700 500"/>
    </g>
    <circle cx="600" cy="383" r="152" fill="none" stroke="#0054AA" stroke-width="5"/>
    <g fill="#0054AA">
      <circle cx="499" cy="272" r="11"/><circle cx="701" cy="272" r="11"/>
      <circle cx="447" cy="383" r="11"/><circle cx="753" cy="383" r="11"/>
      <circle cx="499" cy="494" r="11"/><circle cx="701" cy="494" r="11"/>
    </g>
    <text x="600" y="398" text-anchor="middle" font-family="Open Sans, sans-serif" font-weight="800" font-size="44" fill="#2F74C6">Nestivo</text>
    <g fill="none" stroke="#fff" stroke-width="2">
      <circle cx="133" cy="206" r="37" fill="#0054AA"/><circle cx="126" cy="380" r="37" fill="#0054AA"/><circle cx="133" cy="561" r="37" fill="#0054AA"/>
      <circle cx="1066" cy="206" r="37" fill="#0054AA"/><circle cx="1073" cy="380" r="37" fill="#0054AA"/><circle cx="1066" cy="561" r="37" fill="#0054AA"/>
      <circle cx="133" cy="206" r="32" stroke-width="1.2"/><circle cx="126" cy="380" r="32" stroke-width="1.2"/><circle cx="133" cy="561" r="32" stroke-width="1.2"/>
      <circle cx="1066" cy="206" r="32" stroke-width="1.2"/><circle cx="1073" cy="380" r="32" stroke-width="1.2"/><circle cx="1066" cy="561" r="32" stroke-width="1.2"/>
      <circle cx="133" cy="206" r="13"/><path d="M133 198V206L139 210"/>
      <circle cx="126" cy="380" r="14"/><path d="M119 380L124 386L134 374"/>
      <path d="M120 566a10 10 0 0 1 3-19a12 12 0 0 1 22 3a8 8 0 0 1 0 16Z"/>
      <rect x="1054" y="194" width="24" height="18" rx="2"/><path d="M1062 200l-3 3l3 3M1070 200l3 3l-3 3M1060 218h12"/>
      <path d="M1073 366l12 5v9c0 8-6 12-12 14c-6-2-12-6-12-14v-9Z"/><path d="M1067 380l4 4l8-8"/>
      <rect x="1052" y="548" width="28" height="19" rx="2"/><path d="M1060 573h12M1066 567v6M1060 557l4 4l8-7"/>
    </g>
  </svg>

  <div class="feature">
    <h3 style="left:193px;top:164px">Fast Construction</h3>
    <p style="left:195px;top:213px">From the time the contract is signed and deposit is paid - we can have you living in your new house in under 12 weeks,</p>
    <h3 style="left:195px;top:338px">Affordable</h3>
    <p style="left:195px;top:387px">You can own your own home from under $90 per week. You supply the land - we will supply the house.</p>
    <h3 style="left:193px;top:521px">Quality fit-out</h3>
    <p style="left:195px;top:570px">We have sourced the best quality local and imported products to ensure you the highest quality. If we don't have what you are after our buying team will source it. Our job is to make your dream come true.</p>
    <h3 style="left:769px;top:164px">Minimal Permits</h3>
    <p style="left:770px;top:213px;width:235px">Every council is different but our core construction is pre-engineered in our factories and signed off prior to delivery - this means lees local government bureaucracy.</p>
    <h3 style="left:769px;top:338px">10 Year Guarantee</h3>
    <p style="left:770px;top:387px;width:235px">Australian regulations require builders to give a 7 year builders warranty. We are so confident in our structures we will give you 10 years structural Guarantee - new for old replacement.</p>
    <h3 style="left:769px;top:521px">Stress free building</h3>
    <p style="left:770px;top:570px;width:260px">We have a team of specialists to help you through the very exciting design, build and move in phases of your journey. We have engineers, tradesman, designers and support team to enable you to realise your dream</p>
  </div>
</section>

<section class="services">
  <div class="section-title" style="top:70px;font-size:34px">OUR SERVICES</div>
  <div class="title-bar" style="top:128px"></div>
</section>
<svg class="services-curve" width="1200" height="611">
  <path d="M0 430C10 520 100 611 290 611H0Z" fill="#151515"/>
</svg>
<div class="service-card" style="left:104px">
  <div class="service-photo" role="img" aria-label="Architectural floor plan drawings with pencil and compass" style="background:linear-gradient(135deg,#f4f7fb,#cfdbe9)"></div>
  <h4>Choose your floor<br>plan</h4>
</div>
<div class="service-card" style="left:441px">
  <div class="service-photo" role="img" aria-label="Two-storey grey house exterior with garden path at dusk" style="background:linear-gradient(180deg,#5d6b86,#4f5b6c 55%,#4f7a35)"></div>
  <h4>Choose your exterior<br>design</h4>
</div>
<div class="service-card" style="left:779px">
  <div class="service-photo" role="img" aria-label="Bright interior dining room with wooden table and pendant lights" style="background:linear-gradient(160deg,#f1efec,#d8ccbc 60%,#b08a5e)"></div>
  <h4>Choose your interior<br>design</h4>
</div>

<section class="offer" role="img" aria-label="Dark line sketch of a modern living room interior">
</section>
<div class="offer-line" style="top:2117px;font-size:57px;font-weight:700">WE ARE OFFERING 1,000 HOMES</div>
<div class="offer-line" style="top:2186px;font-size:44px;font-weight:400">(TO ANYWHERE IN THE WORLD)</div>
<div class="offer-line" style="top:2244px;font-size:46px;font-weight:700">FOR US$9,999 + SHIPPING</div>
<div class="offer-line" style="top:2390px;font-size:44px;font-weight:700">NEWSLETTER SIGN UP</div>
<div class="newsletter">Enter your email
  <svg class="abs" style="left:690px;top:14px" width="28" height="26" viewBox="0 0 28 26"><path d="M1 12L27 1L20 25L13 16Z" fill="#0054AA"/><path d="M13 16L27 1" stroke="#fff" stroke-width="1.5"/></svg>
</div>

<footer class="site-footer">
  <svg class="abs" style="left:0;top:0" width="1200" height="433">
    <path d="M0 433V170C0 60 70 0 180 0H1200V433Z" fill="#0558AD"/>
    <line x1="97" y1="372" x2="1100" y2="372" stroke="#4d86c7" stroke-width="1"/>
  </svg>
</footer>
<div class="footer-name">Nestivo</div>
<div class="payments"><span>Cardora</span><span>Paylo</span><span>Debix</span><span>Trevo</span></div>
<div class="foot-head" style="left:403px">Quick Links</div>
<ul class="quick-links">
  <li>Privacy</li><li>Terms &amp; Conditions</li><li>Investment</li><li>Media</li><li>NGO/Government</li><li>Contact</li><li>Sitemap</li>
</ul>
<div class="foot-head" style="left:605px">Get In Touch</div>
<div class="field" style="left:607px;top:2746px;width:241px;height:32px">Name :</div>
<div class="field" style="left:857px;top:2746px;width:241px;height:32px">Phone :</div>
<div class="field" style="left:607px;top:2789px;width:491px;height:32px">Email :</div>
<div class="field" style="left:607px;top:2832px;width:491px;height:72px">Message :</div>
<div class="submit">SUBMIT</div>
<div class="copyright">© copyrights 2022 Nestivo | &nbsp;All Rights Reserved</div>
<div class="socials">
  <span aria-label="Chatterly">C</span><span aria-label="WorkLoop">W</span><span aria-label="ZipZap">Z</span><span class="filled" aria-label="Pictova">P</span><span aria-label="Chirpex">C</span>
</div>

</body>
</html>
```